NorthPlain Bytes Yellow rose letterhead

I have a new logo for my company but in its current form it is too large to be used on letterhead or as a email signature. I need to have the designer use elements from the current logo and create something close to the original but more suited for smaller items.
Updates

I just uploaded a copy of our logo that does not have the weathered affect. Thanks

Industry/Entity Type

It Company

Requirements
Must have
• The design must maintain the visual effect of the current logo. It needs to include the yellow rose and the name of the company.
Nice to have
• It would be nice to maintain the stamp theme and incorporate my name, address, phone, email. etc.

```html
<!DOCTYPE html>
<html lang="en">
<head>
<meta charset="utf-8">
<title>NorthPlain Bytes – Letterhead Stamp</title>
<link rel="stylesheet" href="https://fonts.googleapis.com/css2?family=Delius&display=swap">
<style>
  :root {
    --paper: #ffffff;
    --stamp-gold: #f6c90e;
    --stamp-body: #4b4047;
    --info-yellow: #ecd826;
    --name-grey: #d6ccd1;
  }
  html, body {
    margin: 0;
    padding: 0;
    width: 1200px;
    height: 1000px;
    overflow: hidden;
    background: var(--paper);
  }
  .letterhead {
    position: relative;
    width: 1200px;
    height: 1000px;
  }
  .stamp {
    position: absolute;
    left: 90px;
    top: 26px;
    width: 275px;
    height: 136px;
  }
  .stamp-shape { position: absolute; inset: 0; }
  .brand {
    position: absolute;
    left: 34px;
    top: 12px;
    width: 90px;
    height: 110px;
    font-family: "Delius", sans-serif;
    color: var(--name-grey);
    font-size: 15px;
    line-height: 1;
  }
  .brand-top { position: absolute; left: 0; top: 4px; }
  .brand-bottom { position: absolute; left: 4px; top: 86px; }
  .brand-dot {
    position: absolute;
    left: 6px;
    top: 34px;
    width: 42px;
    height: 42px;
    border-radius: 50%;
    background: var(--stamp-gold);
  }
  .contact {
    position: absolute;
    left: 131px;
    top: 17px;
    font-family: "Delius", sans-serif;
    color: var(--info-yellow);
    font-size: 10.5px;
    line-height: 15.3px;
    white-space: nowrap;
  }
  .contact p { margin: 0; }
  .contact .email {
    font-size: 8px;
    letter-spacing: 0.4px;
    font-variant: small-caps;
    text-transform: lowercase;
    margin-top: 3px;
  }
  .contact .phone { margin-top: 1px; letter-spacing: 0.3px; }
</style>
</head>
<body>
<main class="letterhead">
  <section class="stamp">
    <svg class="stamp-shape" width="275" height="136" viewBox="0 0 275 136" aria-hidden="true">
      <!-- gold frame -->
      <polygon points="10,78 4,110 12,104" fill="var(--stamp-gold)"/>
      <rect x="8" y="4" width="261" height="127" rx="12" fill="var(--stamp-gold)"/>
      <g fill="var(--stamp-gold)">
        <circle cx="24" cy="5" r="4"/><circle cx="40" cy="5" r="4"/><circle cx="56" cy="5" r="4"/>
        <circle cx="72" cy="5" r="4"/><circle cx="88" cy="5" r="4"/><circle cx="104" cy="5" r="4"/>
        <circle cx="120" cy="5" r="4"/><circle cx="136" cy="5" r="4"/><circle cx="152" cy="5" r="4"/>
        <circle cx="168" cy="5" r="4"/><circle cx="184" cy="5" r="4"/><circle cx="200" cy="5" r="4"/>
        <circle cx="216" cy="5" r="4"/><circle cx="232" cy="5" r="4"/><circle cx="248" cy="5" r="4"/>
        <circle cx="24" cy="130" r="4"/><circle cx="40" cy="130" r="4"/><circle cx="56" cy="130" r="4"/>
        <circle cx="72" cy="130" r="4"/><circle cx="88" cy="130" r="4"/><circle cx="104" cy="130" r="4"/>
        <circle cx="120" cy="130" r="4"/><circle cx="136" cy="130" r="4"/><circle cx="152" cy="130" r="4"/>
        <circle cx="168" cy="130" r="4"/><circle cx="184" cy="130" r="4"/><circle cx="200" cy="130" r="4"/>
        <circle cx="216" cy="130" r="4"/><circle cx="232" cy="130" r="4"/><circle cx="248" cy="130" r="4"/>
      </g>
      <!-- dark stamp body -->
      <rect x="16" y="11" width="246" height="114" rx="9" fill="var(--stamp-body)"/>
      <g fill="var(--stamp-gold)">
        <circle cx="32" cy="11" r="4"/><circle cx="48" cy="11" r="4"/><circle cx="64" cy="11" r="4"/>
        <circle cx="80" cy="11" r="4"/><circle cx="96" cy="11" r="4"/><circle cx="112" cy="11" r="4"/>
        <circle cx="128" cy="11" r="4"/><circle cx="144" cy="11" r="4"/><circle cx="160" cy="11" r="4"/>
        <circle cx="176" cy="11" r="4"/><circle cx="192" cy="11" r="4"/><circle cx="208" cy="11" r="4"/>
        <circle cx="224" cy="11" r="4"/><circle cx="240" cy="11" r="4"/>
        <circle cx="32" cy="125" r="4"/><circle cx="48" cy="125" r="4"/><circle cx="64" cy="125" r="4"/>
        <circle cx="80" cy="125" r="4"/><circle cx="96" cy="125" r="4"/><circle cx="112" cy="125" r="4"/>
        <circle cx="128" cy="125" r="4"/><circle cx="144" cy="125" r="4"/><circle cx="160" cy="125" r="4"/>
        <circle cx="176" cy="125" r="4"/><circle cx="192" cy="125" r="4"/><circle cx="208" cy="125" r="4"/>
        <circle cx="224" cy="125" r="4"/><circle cx="240" cy="125" r="4"/>
        <circle cx="16" cy="40" r="3.5"/><circle cx="16" cy="68" r="3.5"/><circle cx="16" cy="96" r="3.5"/>
        <circle cx="262" cy="40" r="3.5"/><circle cx="262" cy="68" r="3.5"/><circle cx="262" cy="96" r="3.5"/>
      </g>
    </svg>

    <div class="brand">
      <span class="brand-top">NorthPlain</span>
      <span class="brand-dot"></span>
      <span class="brand-bottom">Bytes</span>
    </div>

    <address class="contact">
      <p>Mara Lindqvist, PhD</p>
      <p>214 NW Prairie Wind Road</p>
      <p>Ste 1180</p>
      <p>Dalhart, TX 79022</p>
      <p class="email">mara@northplain-bytes.com</p>
      <p class="phone">1-800-555-0147</p>
    </address>
  </section>
</main>
</body>
</html>
```